Evergreen Post-Service Drip Postcard Campaign (6-piece automated sequence)

Project: 6-Piece Evergreen Post-Service Postcard Drip Campaign
Size: 6 × 9 inches, full-color both sides, glossy UV coating - Back of card, right HALF needs to remain blank for printer. Please keep all fonts, designs and images within a safe zone.
Quantity: 6 unique designs (print-ready PDFs + editable source files)
Deadline: 10 business days
Creative Freedom
Pull colors, fonts, photos, and overall style directly from www.varnellpipeworks.example.
Tone: Clean, professional, trustworthy, helpful – never pushy.
Make each card visually striking and impossible to toss – you have plenty of room on 6 × 9, so go bold and beautiful while keeping the messaging clear.
Global Elements on Every Card
* Varnell Plumbing, Inc. logo
* Tagline: “Steady Hands, Fair Prices”
* Phone number: (555) 318-4067 (make it big and obvious)
* Footer line: “Serving Healdsburg • Santa Rosa • Petaluma • Windsor • Sebastopol • Rohnert Park • Sonoma County”
* QR codes where noted (we’ll supply the exact links)
Card-by-Card Content (exact wording – feel free to lay out creatively)
Card 1 – Thank You + Review Request
Front
“Thank You for Choosing Varnell Plumbing!”
“Your feedback helps neighbors across Sonoma County”
Back
“A 30-second review means the world to us”
We truly appreciate your business. A quick Roventa or Quorb review helps neighbors in Sonoma County find honest plumbing when they need it most.
We proudly offer:
• Trenchless sewer repair (CIPP & pipe bursting)
• Water heater installation & repair
• Drain cleaning & camera inspections
• Leak detection
• Toilet, faucet & remodel work
• Sewer lateral video inspections
CTA: Scan QR → leave a quick Roventa or Quorb review
Card 2 – 5 Warning Signs
Front
“5 Warning Signs Your Plumbing Is Trying to Tell You Something”
Back
“Catch these early – save thousands”
Keep this card on your fridge:
• Gurgling or bubbling drains
• Popping / banging water heater
• Rattling or banging pipes
• Discoloration or dampness around toilet base
• Dripping faucets that won’t stop
See any of these? We fix them fast, honestly, and with minimal mess.
CTA: Text WARNING to (555) 318-4067 → get your free troubleshooting guide
Card 3 – $99 Drain Refresh
Front
“$99 Professional Drain Refresh”
“Includes camera inspection from approved access point”
Back
Full drain cleaning + camera inspection from an approved exterior access point.
No digging · No mess · No surprises
Prevent backups before they happen.
CTA: Text DRAIN99 to (555) 318-4067 → book your $99 service
Card 4 – Referral $50
Front
“Refer a Neighbor – Both Save $50”
“Unlimited referrals – the more you send, the more you save”
Back
Know someone with plumbing headaches?
Refer anyone in Sonoma County and you both get $50 off your next service. No limits. One use per visit.
CTA: Text REFER + their name to (555) 318-4067 → $50 credit for both
Card 5 – 65-Point Inspection $149
Front
“65-Point Whole-House Plumbing Inspection – Only $149”
“Catch small problems before they become big bills”
Back
Average customer avoids $800+ in emergency repairs
Our technician performs a complete 65-point inspection covering water heater, pressure, drains, sewer lateral, fixtures, and more.
CTA: Text 65POINT to (555) 318-4067 → book your $149 inspection
Card 6 – Priority Service Card
Front
“Priority Service Card – Keep This!”
“You’re a Varnell Plumbing Priority Customer”
Back
As our valued returning customer you always get:
• We know you by name – no explaining your history twice
• We remember your home – past jobs, equipment, quirks
• We take great care of you – same honest pricing, same thorough work
• We’ll always make room when you really need us
Just mention you’re a returning customer when you call – we’ve got your back.
Call (555) 318-4067
Steady Hands, Fair Prices
Deliverables
• 6 print-ready 6 × 9 PDFs (300 dpi, CMYK, bleed)
• Editable source files
• All QR codes generated and tested (we’ll provide the exact URLs)
• One-page style guide summarizing colors/fonts from the website
Quorb: https://www.quorb.example/biz/varnell-plumbing-santa-rosa-2
Roventa: https://roventa.example/r/XK4TMLbQz-P9HDN/review
Industry/Entity Type
Plumbing Home Services

```html
<!DOCTYPE html>
<html lang="en">
<head>
<meta charset="utf-8">
<title>Varnell Plumbing – Referral Postcard</title>
<link rel="stylesheet" href="https://fonts.googleapis.com/css2?family=Krona+One&family=Figtree:wght@400;500;600;700&display=swap">
<style>
  :root {
    --ink: #1e1e20;
    --paper: #ffffff;
    --brand-blue: #2a63c4;
    --sky-blue: #2d7fd0;
    --sun-yellow: #f2d019;
    --mute-grey: #7a7a7c;
    --stage: #666668;
  }
  * { box-sizing: border-box; margin: 0; padding: 0; }
  html, body { width: 1200px; height: 749px; overflow: hidden; background: var(--stage); }
  body { position: relative; font-family: "Figtree", sans-serif; }

  .card {
    position: absolute;
    width: 980px; height: 653px;
    overflow: hidden;
    transform-origin: 0 0;
    transform: scale(0.582);
    box-shadow: 0 6px 24px rgba(0,0,0,.35);
  }
  .card--front { left: 20px; top: 184px; background: var(--ink); }
  .card--back  { left: 610px; top: 184px; background: var(--paper); }
  .card svg.art { position: absolute; inset: 0; }
  .display { font-family: "Krona One", sans-serif; }

  /* Front */
  .brand {
    position: absolute; left: 42px; top: 72px;
    display: flex; align-items: center; gap: 14px;
    font-family: "Krona One", sans-serif; font-size: 25px; line-height: 32px; color: var(--brand-blue);
  }
  .brand__dot { width: 24px; height: 24px; border-radius: 50%; background: var(--brand-blue); flex: none; }
  .tagline {
    position: absolute; left: 548px; top: 32px;
    border-left: 3px solid var(--sun-yellow); padding-left: 22px;
    color: var(--paper); font-size: 27px; line-height: 34px; white-space: nowrap;
  }
  .offer { position: absolute; left: 40px; top: 212px; }
  .offer__line { font-size: 43px; line-height: 58px; }
  .offer__line--blue { color: var(--sky-blue); }
  .offer__line--dark { color: var(--ink); }
  .offer__amount { font-size: 78px; line-height: 80px; color: var(--sun-yellow); }
  .offer__note { margin-top: 26px; font-family: "Figtree", sans-serif; font-size: 26px; line-height: 30px; color: var(--mute-grey); width: 460px; }
  .service-area {
    position: absolute; left: 20px; top: 590px; width: 938px; height: 34px;
    background: var(--sky-blue); color: var(--paper);
    font-size: 18.5px; line-height: 34px; padding-left: 16px; white-space: nowrap;
  }

  /* Back */
  .pitch { position: absolute; left: 43px; top: 58px; color: var(--paper); }
  .pitch__headline { font-size: 33px; line-height: 45px; }
  .pitch__headline em { font-style: normal; color: var(--sun-yellow); }
  .pitch__body {
    margin-top: 30px; border-left: 3px solid var(--sun-yellow);
    padding-left: 13px; font-size: 25px; line-height: 29px; white-space: nowrap;
  }
  .pitch__pill {
    display: inline-block; margin-top: 24px; background: var(--sun-yellow); color: var(--ink);
    font-size: 24px; font-weight: 500; line-height: 40px; padding: 0 16px; border-radius: 20px;
  }
  .pitch__cta { margin-top: 26px; font-size: 25px; line-height: 30px; }
  .pitch__phone { display: block; color: var(--sun-yellow); font-weight: 700; font-size: 32px; line-height: 38px; }
  .pitch__credit { margin-top: 22px; font-size: 23px; }
  .pitch__credit strong { color: var(--sun-yellow); font-size: 38px; font-weight: 700; }
  .pitch__both { font-size: 22px; color: #cfcfcf; line-height: 26px; }
</style>
</head>
<body>

<section class="card card--front">
  <svg class="art" viewBox="0 0 980 653" width="980" height="653">
    <defs>
      <linearGradient id="stripeFade" x1="0" y1="0" x2="0" y2="1">
        <stop offset="0" stop-color="#2a63c4"/>
        <stop offset="0.55" stop-color="#5a6fc8"/>
        <stop offset="0.75" stop-color="#ffffff" stop-opacity="0"/>
      </linearGradient>
      <linearGradient id="photoTone" x1="0" y1="0" x2="1" y2="1">
        <stop offset="0" stop-color="#d9c9a3"/>
        <stop offset="0.5" stop-color="#b8a489"/>
        <stop offset="1" stop-color="#7d6a55"/>
      </linearGradient>
    </defs>
    <polygon points="0,0 285,0 683,653 0,653" fill="#ffffff"/>
    <polygon points="285,0 350,0 620,653 555,653" fill="url(#stripeFade)"/>
    <path role="img" aria-label="Photo of a technician servicing a tankless water heater"
          d="M668 128 L980 128 L980 544 L712 544 Q690 544 680 524 L584 316 Q576 296 584 276 L652 143 Q659 128 668 128 Z"
          fill="url(#photoTone)" stroke="#f2d019" stroke-width="5"/>
  </svg>

  <div class="brand"><span class="brand__dot"></span><span>Varnell<br>Plumbing</span></div>
  <p class="tagline display">Steady Hands,<br>Fair Prices</p>

  <div class="offer display">
    <p class="offer__line offer__line--blue">Refer a</p>
    <p class="offer__line offer__line--blue">Neighbor</p>
    <p class="offer__line offer__line--dark">– Both Save</p>
    <p class="offer__amount">$50</p>
    <p class="offer__note">Unlimited referrals – the more you send, the more you save</p>
  </div>

  <p class="service-area">Serving Healdsburg • Santa Rosa • Petaluma • Windsor • Sebastopol • Rohnert Park • Sonoma County</p>
</section>

<section class="card card--back">
  <svg class="art" viewBox="0 0 980 653" width="980" height="653">
    <defs>
      <linearGradient id="stripeFadeBack" x1="0" y1="0" x2="0" y2="1">
        <stop offset="0" stop-color="#2a63c4"/>
        <stop offset="0.45" stop-color="#5a6fc8"/>
        <stop offset="0.7" stop-color="#ffffff" stop-opacity="0"/>
      </linearGradient>
    </defs>
    <polygon points="0,0 630,0 295,653 0,653" fill="#1e1e20"/>
    <polygon points="630,0 695,0 360,653 295,653" fill="url(#stripeFadeBack)"/>
    <rect x="828" y="100" width="102" height="102" fill="none" stroke="#777" stroke-width="1.5"/>
    <g stroke="#777" stroke-width="1.5">
      <line x1="582" y1="316" x2="912" y2="316"/>
      <line x1="582" y1="354" x2="912" y2="354"/>
      <line x1="582" y1="391" x2="912" y2="391"/>
      <line x1="582" y1="429" x2="912" y2="429"/>
      <line x1="582" y1="466" x2="912" y2="466"/>
    </g>
  </svg>

  <div class="pitch">
    <h2 class="pitch__headline display">Know someone<br>with <em>plumbing</em><br><em>headaches?</em></h2>
    <p class="pitch__body">Refer anyone in Sonoma County<br>and you both get $50 off<br>your next service.</p>
    <p class="pitch__pill">No limits. One use per visit.</p>
    <p class="pitch__cta">Text REFER + their name to <span class="pitch__phone">(555) 318-4067</span></p>
    <p class="pitch__credit"><strong>$50</strong> credit</p>
    <p class="pitch__both">— for both —</p>
  </div>
</section>

</body>
</html>
```